stationary for business

I need stationary letterhead, invoices ,envelopes etc,. my logo is brightcarry and my contact is 2847 Willow Bend Rd, Dubach, LA 71298, Phone number is 318-555-0148, website [login to view URL]
I want it whimsical but classy. We are the official mover for Cypress Hollow College Athletics and we can use the logo. go to our facebook site [login to view URL]

```html
<!DOCTYPE html>
<html lang="en">
<head>
<meta charset="UTF-8">
<title>Brightcarry Letterhead</title>
<link href="https://fonts.googleapis.com/css2?family=Open+Sans:wght@400;600;800&display=swap" rel="stylesheet">
<style>
  :root {
    --backdrop: #d4d4d4;
    --paper: #ffffff;
    --brand-purple: #3a2c86;
    --brand-yellow: #f2d21b;
    --rule-blue: #6270ab;
    --band-grey: #5a5a5c;
    --ink: #4a4a4a;
  }
  * { margin: 0; padding: 0; box-sizing: border-box; }
  html, body {
    width: 1200px;
    height: 1200px;
    overflow: hidden;
    background: var(--backdrop);
    font-family: "Open Sans", Arial, sans-serif;
  }
  .letterhead {
    position: absolute;
    left: 210px;
    top: 48px;
    width: 780px;
    height: 1104px;
    background: var(--paper);
    box-shadow: 0 6px 24px rgba(0, 0, 0, 0.18);
  }
  .brand {
    position: absolute;
    top: 150px;
    left: 0;
    width: 100%;
    display: flex;
    justify-content: center;
    align-items: center;
    gap: 14px;
  }
  .brand-dot {
    width: 34px;
    height: 34px;
    border-radius: 50%;
    background: var(--brand-yellow);
  }
  .brand-name {
    font-weight: 800;
    font-size: 50px;
    letter-spacing: 0.5px;
    color: var(--brand-purple);
    line-height: 1;
  }
  .footer-rule {
    position: absolute;
    left: 78px;
    right: 80px;
    top: 1020px;
    height: 1.5px;
    background: var(--rule-blue);
  }
  .contact-line {
    position: absolute;
    left: 0;
    width: 100%;
    top: 1033px;
    display: flex;
    justify-content: center;
    gap: 20px;
    font-size: 10.5px;
    color: var(--ink);
  }
  .contact-line .label { font-weight: 600; margin-right: 4px; }
  .social-line {
    position: absolute;
    left: 0;
    width: 100%;
    top: 1052px;
    text-align: center;
    font-size: 10.5px;
    color: var(--ink);
  }
  .base-band {
    position: absolute;
    left: 0;
    bottom: 0;
    width: 100%;
    height: 10px;
    display: flex;
  }
  .base-band .band-purple { flex: 1; background: var(--brand-purple); }
  .base-band .band-grey { flex: 1; background: var(--band-grey); }
</style>
</head>
<body>
  <main class="letterhead">
    <header class="brand">
      <span class="brand-dot"></span>
      <span class="brand-name">Brightcarry</span>
    </header>

    <footer>
      <div class="footer-rule"></div>
      <div class="contact-line">
        <span><span class="label">A:</span>2847 Willow Bend Rd, Dubach, LA 71298 USA</span>
        <span><span class="label">P:</span>318-555-0148</span>
        <span><span class="label">E:</span>info@brightcarry.net</span>
        <span><span class="label">W:</span>www.brightcarry.net</span>
      </div>
      <div class="social-line">www.facebook.com/brightcarryla</div>
      <div class="base-band">
        <span class="band-purple"></span>
        <span class="band-grey"></span>
      </div>
    </footer>
  </main>
</body>
</html>
```